Flyer Design Project

New pest control company starting in southern maryland with the name Pest Raiders. We are going off the same kind of concept as the Shadowchasers. Our slogan is.....killing bugs its what we do best. The telephone number for the business is 240 555 0187. About us....we are a new exciting brand coming to the southern Maryland area offering a safer and more effective solution to pest control. We strive to use the safest and most effective products while providing the best and most effective service. We are a local based company with over ten years experience. As a special to all new Maryland clients we are offering the following coupons. 1. New customers get $100 off initial service which includes a termite inspection with a one year contract. 2. With a one year contract get 50 % off mosquito treatments normally $100 now $50 lawn treatments are done every 30 days. 3. Sign up before May 30th and receive lawn treatments for ticks and fleas up to half an acre included at no additional charge with a signed 1 year contract

Industry/Entity Type

```html
<!DOCTYPE html>
<html lang="en">
<head>
<meta charset="utf-8">
<title>Pest Raiders – Flyer</title>
<link href="https://fonts.googleapis.com/css2?family=Open+Sans:wght@400;600;700;800&display=swap" rel="stylesheet">
<style>
  :root{
    --backdrop:#e4e1dc;
    --paper:#ffffff;
    --brand-blue:#2a3794;
    --brand-red:#e31d2b;
    --deep-red:#a50e14;
    --ink:#1d1d1d;
    --grey-light:#c9c9c9;
    --grey-dark:#4a4a4a;
    --coupon-gold:#f1b02f;
    --coupon-light:#f7cf5d;
  }
  *{box-sizing:border-box;margin:0;padding:0}
  html,body{width:1068px;height:1200px;overflow:hidden}
  body{background:var(--backdrop);font-family:"Open Sans",Arial,sans-serif;color:var(--ink);position:relative}
  .flyer{position:absolute;left:84px;top:25px;width:900px;height:1149px;background:var(--paper);box-shadow:0 6px 24px rgba(0,0,0,.25);overflow:hidden}
  .flyer-art{position:absolute;left:0;top:0;width:900px;height:1149px}
  .brand{position:absolute;right:40px;top:40px;text-align:right}
  .brand-name{font-weight:700;color:var(--ink);font-size:38px;line-height:44px;letter-spacing:.5px}
  .headline{position:absolute;left:0;width:100%;text-align:center}
  .headline-main{top:440px;font-size:68px;font-weight:700;color:var(--brand-red);line-height:70px;padding-left:20px}
  .headline-sub{top:508px;font-size:40px;font-weight:700;color:var(--ink);line-height:44px;padding-left:20px}
  .about{position:absolute;left:20px;width:860px;top:566px;text-align:center;font-size:22px;line-height:28px;color:var(--ink)}
  .coupon{position:absolute;top:727px;width:281px;height:198px;background:linear-gradient(180deg,var(--coupon-light),var(--coupon-gold) 40%);box-shadow:0 8px 10px -4px rgba(0,0,0,.3)}
  .coupon::before{content:"";position:absolute;inset:27px 6px 8px 6px;border:2px dashed var(--brand-red)}
  .coupon::after{content:"";position:absolute;right:0;top:0;border-style:solid;border-width:0 30px 30px 0;border-color:transparent var(--paper) #d9d9d9 transparent}
  .coupon-1{left:19px}.coupon-2{left:313px}.coupon-3{left:607px}
  .coupon-tag{position:absolute;left:10px;top:3px;font-size:16px;font-weight:600;color:var(--ink);letter-spacing:-.3px;line-height:22px}
  .coupon-save{position:absolute;left:22px;top:34px;font-size:27px;font-weight:700;line-height:34px}
  .coupon-amount{position:absolute;left:20px;top:66px;font-size:58px;font-weight:700;color:var(--brand-red);line-height:62px;letter-spacing:-1px}
  .coupon-amount sup{font-size:30px;vertical-align:24px}
  .coupon-terms{position:absolute;left:0;width:100%;top:140px;text-align:center;font-size:17px;font-weight:700;line-height:21px}
  .coupon-signup{position:absolute;left:28px;top:44px;font-size:26px;font-weight:700;line-height:28px}
  .coupon-date{position:absolute;left:28px;top:72px;font-size:24px;font-weight:700;color:var(--brand-red);line-height:28px}
  .coupon-fine{position:absolute;left:0;width:100%;top:112px;text-align:center;font-size:14.5px;font-weight:600;line-height:18px}
  .call-bar{position:absolute;left:0;top:969px;width:100%;height:100px;background:linear-gradient(90deg,var(--brand-red),var(--deep-red));display:flex;align-items:center;justify-content:center;color:#fff;gap:24px}
  .call-label{font-size:40px;font-weight:400}
  .call-number{display:flex;align-items:center;gap:12px;font-size:42px;font-weight:700}
  .website{position:absolute;left:0;width:100%;top:1083px;text-align:center;font-size:25px;font-weight:700;color:var(--ink);padding-left:20px}
</style>
</head>
<body>
<main class="flyer">
  <svg class="flyer-art" viewBox="0 0 675 862" preserveAspectRatio="none">
    <defs>
      <linearGradient id="photoTone" x1="0" y1="0" x2="1" y2="1">
        <stop offset="0" stop-color="#8fa3a6"/>
        <stop offset=".45" stop-color="#c9a98e"/>
        <stop offset="1" stop-color="#6f8a4c"/>
      </linearGradient>
      <linearGradient id="redSweep" x1="0" y1="0" x2="1" y2="0">
        <stop offset="0" stop-color="#e31d2b"/>
        <stop offset="1" stop-color="#9c0c12"/>
      </linearGradient>
      <radialGradient id="bugTone">
        <stop offset="0" stop-color="#6b4a2c"/>
        <stop offset="1" stop-color="#6b4a2c" stop-opacity="0"/>
      </radialGradient>
    </defs>
    <path role="img" aria-label="Photo of a smiling family of three outside their house" d="M0,0 L105,0 C250,35 390,110 468,205 C330,250 150,330 0,412 Z" fill="url(#photoTone)"/>
    <path d="M440,205 C530,185 610,178 675,176 L675,472 C600,380 520,275 440,205 Z" fill="url(#redSweep)"/>
    <path d="M100,0 L170,0 C330,45 520,100 675,126 L675,152 C520,138 330,90 100,0 Z" fill="#cccccc"/>
    <path d="M300,70 C420,120 560,150 675,152 L675,178 C570,182 480,190 440,205 C400,150 350,105 300,70 Z" fill="#4a4a4a"/>
    <ellipse role="img" aria-label="Bee illustration" cx="490" cy="190" rx="30" ry="26" fill="url(#bugTone)"/>
    <ellipse role="img" aria-label="Mosquito illustration" cx="600" cy="205" rx="40" ry="28" fill="url(#bugTone)"/>
    <ellipse role="img" aria-label="Cockroach illustration" cx="470" cy="289" rx="32" ry="14" fill="url(#bugTone)"/>
    <ellipse role="img" aria-label="Fly illustration" cx="613" cy="310" rx="28" ry="22" fill="url(#bugTone)"/>
    <ellipse role="img" aria-label="Mosquito illustration" cx="60" cy="810" rx="40" ry="26" fill="url(#bugTone)" opacity=".8"/>
  </svg>

  <div class="brand">
    <span class="brand-name">Pest Raiders</span>
  </div>

  <h1 class="headline headline-main">KILLING BUGS</h1>
  <h2 class="headline headline-sub">ITS WHAT WE DO BEST</h2>

  <p class="about">We are a new exciting brand coming to the southern Maryland area offering<br>a safer and more effective solution to pest control. We strive to use the safest<br>and most effective products while providing the best and most effective service.<br>We are a local based company with over ten years experience.</p>

  <section class="coupon coupon-1">
    <span class="coupon-tag">NEW CUSTOMERS SPECIAL</span>
    <span class="coupon-save">SAVE</span>
    <span class="coupon-amount"><sup>$</sup>100 off</span>
    <span class="coupon-terms">TERMITE INSPECTION WITH<br>A ONE YEAR CONTRACT</span>
  </section>
  <section class="coupon coupon-2">
    <span class="coupon-tag">NEW CUSTOMERS SPECIAL</span>
    <span class="coupon-save">SAVE</span>
    <span class="coupon-amount"><sup>$</sup>50 off</span>
    <span class="coupon-terms">MOSQUITO TREATMENTS<br>are done every 30 days</span>
  </section>
  <section class="coupon coupon-3">
    <span class="coupon-tag">NEW CUSTOMERS SPECIAL</span>
    <span class="coupon-signup">SIGN UP</span>
    <span class="coupon-date">BEFORE MAY 30TH</span>
    <span class="coupon-fine">and receive lawn treatments for<br>ticks and fleas up to half an acre<br>included at no additional charge<br>with a signed 1 year contract</span>
  </section>

  <div class="call-bar">
    <span class="call-label">CALL US NOW!</span>
    <span class="call-number">
      <svg width="42" height="42" viewBox="0 0 42 42" aria-hidden="true">
        <circle cx="21" cy="21" r="18.5" fill="none" stroke="#fff" stroke-width="3"/>
        <path d="M14 11c1.5-1 3-.5 3.6.8l1.6 3.4c.4.9.1 1.9-.6 2.5l-1.3 1c.9 2.4 2.7 4.3 5.1 5.3l1.1-1.3c.6-.7 1.6-.9 2.5-.5l3.3 1.7c1.2.6 1.6 2.200 .7 3.5-1.3 2-3.6 2.8-5.8 2-5.6-2.1-9.7-6.3-11.6-11.9-.7-2.3.1-4.9 1.4-6.5z" fill="#fff"/>
      </svg>
      240 555 0187
    </span>
  </div>

  <p class="website">WWW.PESTRAIDERSUSA.COM</p>
</main>
</body>
</html>
```